New Property management company business cards

Looking for a new business card, to reflect new younger ownership
Card should be clean, simple and professional but with a modern layout that is conveys our new logo and business model

Key aspects of the business:

Property Management
Facility Maintenance
Project Management
Tenant Improvements

Mailing Address:
PO BOX 7186
Modesto CA, 95353

Phone: 209-614-8837
Direct: 209-614-8831

Doyle Farrant
President

Target Market(s)

Commercial property owners

Industry/Entity Type

Real Estate property management

Contact Information for Business Card

Open to all designs but lean toward vertical layouts

Requirements
Must have
• Logo and space to customize name and contact info

```html
<!DOCTYPE html>
<html lang="en">
<head>
<meta charset="utf-8">
<title>Valmora Property Management – Business Cards</title>
<link href="https://fonts.googleapis.com/css2?family=Poppins:wght@400;600;700&display=swap" rel="stylesheet">
<style>
  :root {
    --page: #ffffff;
    --card-white: #ffffff;
    --ink: #2c2b3a;
    --teal-top: #1a9e96;
    --teal-mid: #12756f;
    --teal-bottom: #093c3c;
    --teal-accent: #22a89e;
    --text-light: #ffffff;
    --icon-fill: #dfe7e6;
  }
  * { box-sizing: border-box; margin: 0; padding: 0; }
  html, body { width: 800px; height: 1200px; overflow: hidden; }
  body {
    background: var(--page);
    font-family: "Poppins", sans-serif;
    position: relative;
  }
  .card {
    position: absolute;
    top: 303px;
    width: 340px;
    height: 594px;
    background: var(--card-white);
    box-shadow: 0 6px 22px rgba(0,0,0,0.18);
    overflow: hidden;
  }
  .card--services { left: 45px; }
  .card--contact { left: 415px; }
  .card-bg { position: absolute; inset: 0; width: 100%; height: 100%; }

  .brand {
    position: absolute;
    left: 0; right: 0;
    top: 70px;
    display: flex;
    align-items: center;
    justify-content: center;
    gap: 10px;
    color: var(--ink);
    font-weight: 600;
  }
  .brand-square {
    width: 30px; height: 30px;
    background: var(--teal-accent);
  }
  .brand-name { display: flex; flex-direction: column; line-height: 1; }
  .brand-name__main { font-size: 34px; letter-spacing: 5px; }
  .brand-name__sub { font-size: 8.5px; letter-spacing: 3.6px; margin-top: 6px; }

  .centered {
    position: absolute;
    left: 0; right: 0;
    text-align: center;
    transform: translateY(-50%);
    color: var(--text-light);
  }
  .diamond {
    position: absolute;
    left: 50%;
    width: 43px; height: 43px;
    transform: translate(-50%, -50%);
  }
  .service-label { font-size: 12.5px; font-weight: 600; }

  .web-pill {
    position: absolute;
    left: 20px; top: 538px;
    width: 299px; height: 23px;
    background: var(--card-white);
    border-radius: 12px;
    color: var(--ink);
    font-size: 12.5px;
    font-weight: 600;
    letter-spacing: 1.9px;
    text-align: center;
    line-height: 23px;
  }

  .person-name { font-size: 38px; font-weight: 700; letter-spacing: -0.5px; line-height: 1; }
  .person-title { font-size: 21px; font-weight: 400; line-height: 1; }
  .divider {
    position: absolute;
    left: 44px; top: 318px;
    width: 252px; height: 1px;
    background: rgba(255,255,255,0.7);
  }
  .divider::after {
    content: "";
    position: absolute;
    left: 50%; top: -2px;
    width: 60px; height: 5px;
    transform: translateX(-50%);
    background: var(--text-light);
    border-radius: 3px;
  }
  .contact-line { font-size: 11.5px; font-weight: 600; }
</style>
</head>
<body>

  <!-- Services side -->
  <section class="card card--services">
    <svg class="card-bg" viewBox="0 0 632 1105" preserveAspectRatio="none" aria-hidden="true">
      <defs>
        <linearGradient id="tealFillA" x1="0" y1="0" x2="0" y2="1">
          <stop offset="0" stop-color="#1a9e96"/>
          <stop offset="0.5" stop-color="#12756f"/>
          <stop offset="1" stop-color="#093c3c"/>
        </linearGradient>
      </defs>
      <polygon points="0,335 316,405 632,335 632,1105 0,1105" fill="url(#tealFillA)"/>
      <polygon points="632,420 632,760 260,1105 0,1105" fill="#ffffff" opacity="0.04"/>
      <polygon points="0,310 316,380 632,310 632,330 316,400 0,330" fill="#2c2b3a"/>
    </svg>

    <div class="brand">
      <span class="brand-square"></span>
      <span class="brand-name">
        <span class="brand-name__main">VALMORA</span>
        <span class="brand-name__sub">PROPERTY MANAGEMENT</span>
      </span>
    </div>

    <svg class="diamond" style="top:266px" viewBox="0 0 43 43" role="img" aria-label="Property management icon">
      <polygon points="21.5,1 42,21.5 21.5,42 1,21.5" fill="#fff"/>
      <polygon points="21.5,5 38,21.5 21.5,38 5,21.5" fill="none" stroke="#22a89e" stroke-width="1.5"/>
      <circle cx="21.5" cy="21.5" r="8" fill="var(--icon-fill)"/>
    </svg>
    <div class="centered service-label" style="top:300px">Property Management</div>

    <svg class="diamond" style="top:331px" viewBox="0 0 43 43" role="img" aria-label="Facility maintenance icon">
      <polygon points="21.5,1 42,21.5 21.5,42 1,21.5" fill="#fff"/>
      <polygon points="21.5,5 38,21.5 21.5,38 5,21.5" fill="none" stroke="#22a89e" stroke-width="1.5"/>
      <circle cx="21.5" cy="21.5" r="8" fill="var(--icon-fill)"/>
    </svg>
    <div class="centered service-label" style="top:362px">Facility Maintenance</div>

    <svg class="diamond" style="top:403px" viewBox="0 0 43 43" role="img" aria-label="Project management icon">
      <polygon points="21.5,1 42,21.5 21.5,42 1,21.5" fill="#fff"/>
      <polygon points="21.5,5 38,21.5 21.5,38 5,21.5" fill="none" stroke="#22a89e" stroke-width="1.5"/>
      <circle cx="21.5" cy="21.5" r="8" fill="var(--icon-fill)"/>
    </svg>
    <div class="centered service-label" style="top:437px">Project Management</div>

    <svg class="diamond" style="top:468px" viewBox="0 0 43 43" role="img" aria-label="Tenant improvements icon">
      <polygon points="21.5,1 42,21.5 21.5,42 1,21.5" fill="#fff"/>
      <polygon points="21.5,5 38,21.5 21.5,38 5,21.5" fill="none" stroke="#22a89e" stroke-width="1.5"/>
      <circle cx="21.5" cy="21.5" r="8" fill="var(--icon-fill)"/>
    </svg>
    <div class="centered service-label" style="top:504px">Tenant Improvements</div>

    <div class="web-pill">www.valmoraproperties.com</div>
  </section>

  <!-- Contact side -->
  <section class="card card--contact">
    <svg class="card-bg" viewBox="0 0 632 1105" preserveAspectRatio="none" aria-hidden="true">
      <defs>
        <linearGradient id="tealFillB" x1="0" y1="0" x2="0" y2="1">
          <stop offset="0" stop-color="#1a9e96"/>
          <stop offset="0.5" stop-color="#12756f"/>
          <stop offset="1" stop-color="#093c3c"/>
        </linearGradient>
      </defs>
      <polygon points="0,335 316,405 632,335 632,1105 0,1105" fill="url(#tealFillB)"/>
      <polygon points="632,420 632,760 260,1105 0,1105" fill="#ffffff" opacity="0.04"/>
      <polygon points="0,310 316,380 632,310 632,330 316,400 0,330" fill="#2c2b3a"/>
    </svg>

    <div class="brand">
      <span class="brand-square"></span>
      <span class="brand-name">
        <span class="brand-name__main">VALMORA</span>
        <span class="brand-name__sub">PROPERTY MANAGEMENT</span>
      </span>
    </div>

    <div class="centered person-name" style="top:261px">Doyle Farrant</div>
    <div class="centered person-title" style="top:293px">President</div>
    <div class="divider"></div>

    <svg class="diamond" style="top:371px" viewBox="0 0 43 43" aria-hidden="true">
      <polygon points="21.5,1 42,21.5 21.5,42 1,21.5" fill="#fff"/>
      <polygon points="21.5,5 38,21.5 21.5,38 5,21.5" fill="none" stroke="#22a89e" stroke-width="1.5"/>
      <path d="M16.5 15.5 l3 -1 l1.8 3.6 l-1.8 1.3 q1.2 2.6 3.4 3.8 l1.4 -1.7 l3.5 1.9 l-0.9 3 q-6.8 0.4 -10.4 -10.9z" fill="#2c2b3a"/>
    </svg>
    <div class="centered contact-line" style="top:405px">209-614-8837</div>

    <svg class="diamond" style="top:444px" viewBox="0 0 43 43" aria-hidden="true">
      <polygon points="21.5,1 42,21.5 21.5,42 1,21.5" fill="#fff"/>
      <polygon points="21.5,5 38,21.5 21.5,38 5,21.5" fill="none" stroke="#22a89e" stroke-width="1.5"/>
      <path d="M16.5 15.5 l3 -1 l1.8 3.6 l-1.8 1.3 q1.2 2.6 3.4 3.8 l1.4 -1.7 l3.5 1.9 l-0.9 3 q-6.8 0.4 -10.4 -10.9z" fill="#2c2b3a"/>
    </svg>
    <div class="centered contact-line" style="top:477px">Direct: 209-614-8831</div>

    <svg class="diamond" style="top:516px" viewBox="0 0 43 43" aria-hidden="true">
      <polygon points="21.5,1 42,21.5 21.5,42 1,21.5" fill="#fff"/>
      <polygon points="21.5,5 38,21.5 21.5,38 5,21.5" fill="none" stroke="#22a89e" stroke-width="1.5"/>
      <path d="M21.5 13.5 a5.5 5.5 0 0 1 5.5 5.5 c0 4 -5.5 10 -5.5 10 s-5.5 -6 -5.5 -10 a5.5 5.5 0 0 1 5.5 -5.5z" fill="#2c2b3a"/>
      <circle cx="21.5" cy="19" r="2" fill="#fff"/>
    </svg>
    <div class="centered contact-line" style="top:550px">PO BOX 7186 Modesto CA, 95353</div>
  </section>

</body>
</html>
```